Beer Can Label named: ZAP Ginger Beer

We need a funky design for a Ginger Beer that is made from all natural ingredients. The label needs to be full of Colour, emphasis on the Ginger Root. ZAP (Zested And Poured)

Target Market(s)

None beer drinkers'

Requirements
Must have
• Name on the label must beer easy to read. Needs to be very colourful, playful & even a bit cheaky.
Nice to have
• A label that looks at the benefits of Ginger for the body in a fun artistic design.
Should not have
• Should NOT be a simple, basic, minimalistic design

```html
<!DOCTYPE html>
<html lang="en">
<head>
<meta charset="utf-8">
<title>ZAP Ginger Beer – Can Label</title>
<link rel="stylesheet" href="https://fonts.googleapis.com/css2?family=Roboto+Condensed:wght@400;700;900&display=swap">
<style>
  :root {
    --peach: #f4d49e;
    --cream: #fdf7d8;
    --lemon: #f9ec6c;
    --gold: #ecc233;
    --amber: #e6a92e;
    --orange: #dc7b2a;
    --purple: #82288a;
    --forest: #256b3f;
    --yellow-outline: #fff23a;
    --bronze: #a8823a;
    --tag-red: #d42a2a;
    --bubble-line: #de7033;
    --ink: #2f2f2f;
  }
  html, body {
    margin: 0;
    padding: 0;
    width: 1200px;
    height: 1200px;
    overflow: hidden;
    background: #ffffff;
  }
  .label {
    display: block;
    width: 1200px;
    height: 1200px;
  }
  .brand-name {
    font-family: "Roboto Condensed", sans-serif;
    font-weight: 900;
    fill: var(--forest);
  }
  .product-line {
    font-family: "Roboto Condensed", sans-serif;
    font-weight: 900;
  }
  .product-ginger {
    fill: var(--bronze);
    stroke: var(--yellow-outline);
    stroke-width: 14;
    stroke-linejoin: round;
    paint-order: stroke;
  }
  .product-beer { fill: var(--purple); }
  .tagline-box { fill: var(--tag-red); }
  .tagline-text {
    font-family: "Roboto Condensed", sans-serif;
    font-weight: 700;
    font-size: 29px;
    fill: #ffffff;
  }
  .bubble {
    fill: none;
    stroke: var(--bubble-line);
    stroke-width: 3.5;
    stroke-linejoin: round;
  }
  .bubble-text {
    font-family: "Roboto Condensed", sans-serif;
    font-weight: 400;
    font-size: 23px;
    fill: var(--ink);
    text-anchor: middle;
  }
  .bubble-text.small { font-size: 20px; }
</style>
</head>
<body>
<svg class="label" viewBox="0 0 1200 1200" xmlns="http://www.w3.org/2000/svg">
  <defs>
    <linearGradient id="sky" x1="0" y1="0" x2="1" y2="0.4">
      <stop offset="0" stop-color="var(--peach)"/>
      <stop offset="0.42" stop-color="var(--cream)"/>
      <stop offset="1" stop-color="var(--lemon)"/>
    </linearGradient>
    <linearGradient id="slope" x1="0" y1="1" x2="1" y2="0">
      <stop offset="0" stop-color="var(--amber)"/>
      <stop offset="1" stop-color="var(--gold)"/>
    </linearGradient>
    <linearGradient id="wave" x1="0" y1="0" x2="1" y2="0">
      <stop offset="0" stop-color="var(--orange)"/>
      <stop offset="0.55" stop-color="#e38f2c"/>
      <stop offset="1" stop-color="var(--gold)"/>
    </linearGradient>
    <radialGradient id="root-tone" cx="0.45" cy="0.45" r="0.6">
      <stop offset="0" stop-color="#fbf1c6"/>
      <stop offset="0.7" stop-color="#ecd08a"/>
      <stop offset="1" stop-color="#ecd08a" stop-opacity="0"/>
    </radialGradient>
    <radialGradient id="leaf-tone" cx="0.5" cy="0.5" r="0.55">
      <stop offset="0" stop-color="#6fa83a"/>
      <stop offset="0.75" stop-color="#3f7d2b"/>
      <stop offset="1" stop-color="#3f7d2b" stop-opacity="0"/>
    </radialGradient>
  </defs>

  <!-- background -->
  <rect class="bg-sky" width="1200" height="1085" fill="url(#sky)"/>
  <path class="bg-slope" d="M1200,515 L0,1010 L0,1085 L1200,1085 Z" fill="url(#slope)"/>
  <path class="bg-wave" d="M0,905 C70,990 190,1012 340,992 C600,958 900,920 1200,880 L1200,1085 L0,1085 Z" fill="url(#wave)" opacity="0.9"/>
  <rect class="base-band" y="1085" width="1200" height="115" fill="var(--purple)"/>

  <!-- brand name -->
  <text class="brand-name" x="285" y="560" font-size="230" textLength="270" lengthAdjust="spacingAndGlyphs">ZAP</text>

  <!-- product line -->
  <text class="product-line product-ginger" x="585" y="325" font-size="135" textLength="335" lengthAdjust="spacingAndGlyphs">Ginger</text>
  <text class="product-line product-beer" x="588" y="494" font-size="205" textLength="340" lengthAdjust="spacingAndGlyphs">Beer</text>

  <!-- tagline -->
  <rect class="tagline-box" x="284" y="729" width="276" height="40"/>
  <text class="tagline-text" x="422" y="760" text-anchor="middle" textLength="262" lengthAdjust="spacingAndGlyphs">Zested And Poured</text>

  <!-- artwork areas -->
  <ellipse class="art-ginger-root" role="img" aria-label="Illustration of a fresh ginger root with sliced pieces"
           cx="740" cy="650" rx="190" ry="140" fill="url(#root-tone)"/>
  <ellipse class="art-leaf" role="img" aria-label="Photo of a green ginger leaf on a stem"
           cx="390" cy="945" rx="95" ry="115" fill="url(#leaf-tone)"/>

  <!-- benefit bubbles -->
  <g class="benefit benefit-digestion">
    <path class="bubble" d="M980,669 C930,672 890,640 885,590 C880,535 935,505 1005,505 C1085,505 1128,545 1126,590 C1124,640 1075,672 1015,670 L955,682 Z"/>
    <text class="bubble-text" x="1003" y="557">Reducing gas and</text>
    <text class="bubble-text" x="1003" y="581">improving digestion</text>
    <text class="bubble-text small" x="1008" y="609">Easing a cold or the flu</text>
  </g>

  <g class="benefit benefit-pain">
    <path class="bubble" d="M958,838 C922,810 925,740 990,720 C1060,700 1137,728 1136,790 C1135,850 1070,865 1025,862 C995,860 975,855 965,848 L900,850 Z"/>
    <text class="bubble-text" x="1030" y="766">Relieving pain</text>
    <text class="bubble-text" x="1030" y="799">Reducing</text>
    <text class="bubble-text" x="1030" y="828">inflammation</text>
  </g>

  <g class="benefit benefit-cancer">
    <path class="bubble" d="M600,792 C660,795 702,818 700,858 C698,900 640,917 585,915 C520,913 472,890 475,852 C478,815 530,792 585,792 L615,752 L630,752 Z"/>
    <text class="bubble-text" x="587" y="861">Lowering cancer risk</text>
  </g>

  <g class="benefit benefit-heart">
    <ellipse class="bubble" cx="742" cy="1003" rx="127" ry="70"/>
    <ellipse class="bubble" cx="742" cy="1003" rx="122" ry="66" transform="rotate(-3 742 1003)"/>
    <circle class="bubble" cx="798" cy="890" r="13"/>
    <circle class="bubble" cx="834" cy="868" r="8"/>
    <circle class="bubble" cx="866" cy="850" r="5"/>
    <text class="bubble-text" x="738" y="992">Supporting</text>
    <text class="bubble-text" x="740" y="1020">cardiovascular health</text>
  </g>
</svg>
</body>
</html>
```